Life Insurance Landing Page (for lead gen)

We need a high converting life insurance page created. It will be housed at www.CoverCheckpoint.com. We will be driving former life insurance prospects to this page where they will only need to confirm their phone number & email in order to receive an updated quote.
Updates

Only the page design is required, the coding will be done on our end. 

Target Market(s)

People who have expressed an interest in obtaining life insurance.

Industry/Entity Type

Life Insurance

Requirements
Must have
• 1) Under "CoverCheckpoint.com" Please include a "Powered by TPVN" tag and match the colors of this site: http://thetpvn.com/life-insurance-services.html to the page.

2) The form should ask for their phone number and include an appointment calendar widget (we'll code the functionality) so they can choose the date/time of their call. It should also have an email confirmation field.

3) the overall message next to the form fields should be "Thanks for visiting Gordon (we'll personalize this "firstname" field ), please let us know the best time to schedule a brief call so we can give you an updated, rock bottom pricing quote on a policy. We'll also email you with the information, please confirm your email here and we'll send you the details.

4) We'd like to include a box that appears to be a personalized "quote briefing" snapshot that will list this information: "Name: _________" "Birth Date:"____________" "Policy Type: _______", "Coverage Amount: ____________" " all these fields will be populated into the page.

```html
<!DOCTYPE html>
<html lang="en">
<head>
<meta charset="utf-8">
<title>CoverCheckpoint.com – Life Insurance Quote</title>
<link href="https://fonts.googleapis.com/css2?family=Arimo:wght@400;700&family=Open+Sans:wght@300&family=Oswald:wght@400;500&display=swap" rel="stylesheet">
<style>
:root{
  --page-bg:#ececec;
  --panel:#ffffff;
  --brand:#1b8ad3;
  --brand-dark:#0b69ad;
  --heading:#0d6db3;
  --rule:#1f78bd;
  --text:#5a5f64;
  --text-dark:#222;
  --field-border:#c9cdd1;
  --bullet:#1b8ad3;
  --grey-head:#b7b7b7;
  --news-head:#0e5d95;
  --news-body:#1c84c6;
  --news-btn:#34c3e6;
  --cal-select:#3aa0e8;
}
*{box-sizing:border-box;margin:0;padding:0}
html,body{width:1200px;height:2172px;overflow:hidden}
body{background:var(--page-bg);font-family:"Arimo",Arial,sans-serif;color:var(--text);position:relative}
.panel{position:absolute;left:188px;width:823px;background:var(--panel)}

/* header */
.site-header{top:8px;height:67px;border-bottom:4px solid var(--rule)}
.brand{position:absolute;left:16px;top:7px;font-weight:700;font-size:31px;color:var(--brand);letter-spacing:-.3px;line-height:36px}
.brand-tag{position:absolute;left:126px;top:42px;font-size:15px;font-weight:700;color:#555;line-height:18px}
.social{position:absolute;right:22px;top:28px;display:flex;gap:8px}
.social span{width:12px;height:12px;border-radius:50%;background:#b8c4cc}

/* hero */
.hero{top:93px;height:440px}
.hero-photo{position:absolute;left:19px;top:20px;width:285px;height:420px;background:linear-gradient(180deg,#e9e2da 0%,#d9cfc4 45%,#8fb5d6 75%,#4b5b6c 100%);border-radius:4px}
.hero-title{position:absolute;left:318px;top:34px;font-family:"Open Sans",Arial,sans-serif;font-weight:300;font-size:40px;color:var(--brand-dark);letter-spacing:-1px;line-height:52px;white-space:nowrap}
.hero-copy{position:absolute;left:325px;top:92px;width:480px;font-size:14.5px;line-height:19px;color:#333}
.hero-copy p+p{margin-top:19px}
.lead-form{position:absolute;left:327px;top:200px;width:467px;height:210px;border:1.5px solid #4a9ad6;border-radius:5px}
.field{position:absolute;left:15px;width:173px;height:26px;border:1px solid var(--field-border);border-radius:2px;font-size:12px;color:#888;padding:5px 9px;background:#fff}
.btn-submit{position:absolute;left:16px;top:152px;width:92px;height:31px;border-radius:3px;background:linear-gradient(#2a86c8,#145f9a);color:#fff;font-size:14px;font-weight:700;text-align:center;line-height:31px}
.label{position:absolute;font-size:12.5px;color:#555}
.icon{position:absolute}
.date-field{position:absolute;left:327px;top:21px;width:90px;height:26px;border:1px solid var(--field-border);background:#f1f1f1;font-size:12px;color:#555;padding:5px 9px}
.time-field{position:absolute;left:327px;top:64px;width:90px;height:26px;border:1px solid var(--field-border);background:#f6f6f6;font-size:12px;color:#bbb;padding:5px 9px}

/* calendar */
.calendar{position:absolute;left:779px;top:346px;width:324px;height:218px;background:rgba(255,255,255,.97);border:1px solid #d3d3d3;box-shadow:0 2px 10px rgba(0,0,0,.2);font-size:11px;color:#222}
.cal-head{position:absolute;left:0;top:8px;width:100%;text-align:center;font-size:13px}
.cal-head em{color:#888;font-style:italic}
.cal-prev,.cal-next{position:absolute;top:8px;font-size:12px}
.cal-prev{left:12px}.cal-next{right:12px}
.cal-grid{position:absolute;left:6px;top:30px;width:312px;border-collapse:collapse}
.cal-grid th{font-weight:400;font-size:9.5px;color:#999;height:16px}
.cal-grid td{text-align:center;height:22.6px;width:44.5px}
.cal-grid td.out{color:#c8c8c8}
.cal-grid td.today{color:var(--brand)}
.cal-grid td.sel span{display:inline-block;width:26px;height:20px;line-height:20px;background:var(--cal-select);color:#fff;font-weight:700}
.cal-foot{position:absolute;bottom:10px;left:0;width:100%;font-size:10px;font-weight:700}
.cal-foot .today{position:absolute;left:75px}
.cal-foot .clear{position:absolute;left:212px}
.cal-foot .clear b{color:#e02a2a}

/* intro */
.intro{top:573px;height:264px;border-bottom:4px solid var(--rule)}
.section-title{font-size:29px;font-weight:400;color:var(--heading);line-height:34px}
.intro .section-title{position:absolute;left:32px;top:27px}
.intro-photo{position:absolute;left:35px;top:78px;width:132px;height:137px;background:linear-gradient(180deg,#f5e67a 0%,#e2c543 40%,#a9a13a 70%,#6b8e2e 100%)}
.intro-sub{position:absolute;left:183px;top:75px;font-size:11.5px;color:var(--text-dark)}
.intro-body{position:absolute;left:183px;top:103px;width:356px;font-size:11px;line-height:15.5px}
.intro-body p+p{margin-top:15px}
.offer{position:absolute;left:575px;top:30px;height:200px;padding-left:39px;border-left:1px solid #ddd}
.offer h2{font-size:21px;font-weight:400;color:var(--heading);line-height:30px}
.offer ul{list-style:none;margin-top:6px}
.offer li{font-size:11.5px;color:var(--text-dark);height:23px;position:relative;padding-left:11px}
.offer li::before{content:"";position:absolute;left:0;top:5px;width:5px;height:5px;border-radius:50%;background:var(--bullet)}

/* article */
.article{top:854px;height:1242px;border-bottom:4px solid var(--rule)}
.article-main{position:absolute;left:32px;top:28px;width:508px;font-size:11px;line-height:15px}
.article-main h3{font-size:18.5px;font-weight:400;color:var(--heading);line-height:24px;margin-bottom:8px}
.article-main section{padding-bottom:16px;border-bottom:1px solid #ddd;margin-bottom:16px}
.article-main section:last-child{border-bottom:0;margin-bottom:0}
.article-main p+p{margin-top:14px}
.change-list{list-style:none;margin-top:12px}
.change-list li{height:23px;position:relative;padding-left:11px;color:#333}
.change-list li::before{content:"";position:absolute;left:0;top:5px;width:5px;height:5px;border-radius:50%;background:var(--bullet)}
.sidebar{position:absolute;left:574px;top:0;height:1200px;border-left:1px solid #ddd;padding-left:41px;padding-top:40px;width:220px}

.quote-box{width:177px;height:324px;border:1px solid #ddd;background:#fff}
.quote-box h4{height:42px;background:var(--grey-head);color:#fff;font-family:"Oswald",Arial,sans-serif;font-weight:400;font-size:24px;text-align:center;line-height:42px}
.quote-field{padding:0 13px;margin-top:14px}
.quote-field span{display:block;font-size:11px;color:#555;margin-bottom:5px}
.quote-field i{display:block;height:26px;border:1px solid var(--field-border)}
.quote-btn{margin:18px auto 0;width:100px;height:28px;background:linear-gradient(#f3f3f3,#d6d6d6);border:1px solid #ccc;color:#777;text-align:center;line-height:26px;font-size:13px}

.promo{margin-top:28px;width:177px;height:367px;position:relative;background:linear-gradient(180deg,#2aa05a 0%,#1f8c7b 25%,#1a6fae 60%,#1569ab 100%);overflow:hidden}
.promo h4{position:absolute;top:10px;width:100%;text-align:center;font-family:"Oswald",Arial,sans-serif;font-weight:500;font-size:28px;color:#fff}
.promo p{position:absolute;top:64px;left:8px;width:161px;text-align:center;color:#fff;font-size:14px;line-height:19px}
.promo-photo{position:absolute;left:0;top:140px;width:177px;height:190px;background:linear-gradient(180deg,#2c7ab3 0%,#b9cfe0 45%,#f1f1f1 100%)}
.promo-cta{position:absolute;bottom:0;width:100%;height:38px;background:#1b6db1;color:#fff;font-family:"Oswald",Arial,sans-serif;font-size:20px;text-align:center;line-height:38px}

.newsletter{margin-top:26px;width:177px;height:171px;background:var(--news-body);border:1px solid #1a75b0}
.newsletter h4{height:42px;background:var(--news-head);color:#fff;font-family:"Oswald",Arial,sans-serif;font-weight:400;font-size:20px;text-align:center;line-height:42px}
.newsletter span{display:block;text-align:center;color:#fff;font-size:12px;margin-top:14px}
.newsletter i{display:block;margin:6px auto 0;width:152px;height:26px;background:#fff}
.news-btn{margin:18px auto 0;width:94px;height:31px;background:var(--news-btn);border:1px solid #1d9fc4;color:#fff;font-size:14px;text-align:center;line-height:29px}

.site-footer{position:absolute;left:188px;width:823px;top:2110px;text-align:center;font-size:10.5px;line-height:14px;color:#333}
</style>
</head>
<body>

<header class="panel site-header">
  <div class="brand">CoverCheckpoint.com</div>
  <div class="brand-tag">Powered by TPVN</div>
  <div class="social"><span></span><span></span><span></span></div>
</header>

<section class="panel hero">
  <div class="hero-photo" role="img" aria-label="Photo of a smiling family: father, mother and young son"></div>
  <h1 class="hero-title">Thanks for visiting Gordon</h1>
  <div class="hero-copy">
    <p>Please let us know the best time to schedule a brief call so we can give you an updated, rock bottom pricing quote on a policy.</p>
    <p>We'll also email you with the information, please confirm your email here and we'll send you the details.</p>
  </div>
  <form class="lead-form">
    <div class="field" style="top:20px">Name</div>
    <div class="field" style="top:62px">Phone</div>
    <div class="field" style="top:105px">Email</div>
    <div class="btn-submit">Submit</div>
    <span class="label" style="left:220px;top:26px">Select date:</span>
    <svg class="icon" style="left:292px;top:21px" width="24" height="24" viewBox="0 0 24 24">
      <rect x="2" y="4" width="20" height="18" rx="2" fill="#2f8fd3"/>
      <rect x="5" y="9" width="14" height="10" fill="#fff"/>
      <rect x="6" y="2" width="2" height="5" fill="#1a6aa8"/><rect x="16" y="2" width="2" height="5" fill="#1a6aa8"/>
      <rect x="7" y="11" width="3" height="2" fill="#2f8fd3"/><rect x="11" y="11" width="3" height="2" fill="#2f8fd3"/><rect x="15" y="11" width="3" height="2" fill="#2f8fd3"/>
      <rect x="7" y="15" width="3" height="2" fill="#2f8fd3"/><rect x="11" y="15" width="3" height="2" fill="#2f8fd3"/>
    </svg>
    <div class="date-field">05/04/2014</div>
    <span class="label" style="left:220px;top:69px">Select Time:</span>
    <svg class="icon" style="left:292px;top:64px" width="24" height="24" viewBox="0 0 24 24">
      <circle cx="12" cy="12" r="10" fill="#e9f3fb" stroke="#4aa0dc" stroke-width="2"/>
      <path d="M12 6v6l4 3" stroke="#4aa0dc" stroke-width="2" fill="none"/>
    </svg>
    <div class="time-field">08:59 PM</div>
  </form>
</section>

<div class="calendar">
  <span class="cal-prev">◀</span>
  <div class="cal-head">April <em>2014</em></div>
  <span class="cal-next">▶</span>
  <table class="cal-grid">
    <tr><th>Sun</th><th>Mon</th><th>Tue</th><th>Wed</th><th>Thu</th><th>Fri</th><th>Sat</th></tr>
    <tr><td class="out">31</td><td>1</td><td>2</td><td>3</td><td class="today">4</td><td class="sel"><span>5</span></td><td>6</td></tr>
    <tr><td>7</td><td>8</td><td>9</td><td>10</td><td>11</td><td>12</td><td>13</td></tr>
    <tr><td>14</td><td>15</td><td>16</td><td>17</td><td>18</td><td>19</td><td>20</td></tr>
    <tr><td>21</td><td>22</td><td>23</td><td>24</td><td>25</td><td>26</td><td>27</td></tr>
    <tr><td>28</td><td>29</td><td>30</td><td class="out">1</td><td class="out">2</td><td class="out">3</td><td class="out">4</td></tr>
    <tr><td class="out">5</td><td class="out">6</td><td class="out">7</td><td class="out">8</td><td class="out">9</td><td class="out">10</td><td class="out">11</td></tr>
  </table>
  <div class="cal-foot"><span class="today">▾ Today</span><span class="clear"><b>✕</b> Clear</span></div>
</div>

<section class="panel intro">
  <h2 class="section-title">Life Insurance</h2>
  <div class="intro-photo" role="img" aria-label="Photo of a family jumping in a sunny park"></div>
  <div class="intro-sub">Linden California - What You Need To Know About Life Insurance</div>
  <div class="intro-body">
    <p>Having the right life insurance is pivotal in planning for the future of you and your loved ones. Life insurance can help you fulfill promises you've made your family when you are gone.</p>
    <p>Don't leave the future of you and your loved ones to chance. TriPoint Valley Insurance Services can help you find the right life insurance coverage for you, and help ensure that your policy continually meets your needs.</p>
  </div>
  <div class="offer">
    <h2>What We Offer</h2>
    <ul>
      <li>Auto Insurance</li><li>Home Insurance</li><li>Life Insurance</li><li>Health Insurance</li>
      <li>Business Insurance</li><li>Restaurant Insurance</li><li>Workers Comp</li>
    </ul>
  </div>
</section>

<section class="panel article">
  <div class="article-main">
    <section>
      <h3>Life changes - so should your policy</h3>
      <p>For each of our neighbors in California, the right life insurance will be unique for you and dependent on your personal and financial needs. As your life changes, your life insurance coverage may need to change in order to adapt to your current needs. Some life transformations that may require a policy "tune-up" and our help at TriPoint Valley Insurance Services include:</p>
      <ul class="change-list">
        <li>You recently married or divorced</li>
        <li>You have a new child or grandchild</li>
        <li>You have opened or expanded a business</li>
        <li>Your health or your spouse's health has deteriorated</li>
        <li>You are providing care or financial assistance to a parent</li>
        <li>Your child or grandchild requires assistance or long-term care</li>
        <li>You recently purchased a new home</li>
        <li>You are planning for a child or grandchild's education</li>
        <li>You are concerned about retirement income</li>
        <li>You have refinanced your home mortgage in the past six months</li>
        <li>You or your spouse recently received an inheritance</li>
        <li>You have a sizable estate</li>
      </ul>
    </section>
    <section>
      <h3>California - what you need to know about life insurance</h3>
      <p>TPVN can help you select the best life insurance coverage for your needs. There are several different types of life insurance products available – the most common include:</p>
    </section>
    <section>
      <h3>Term Life Insurance</h3>
      <p>Term life insurance provides protection for a specified period of time. If you do not currently have life insurance, term can be a good place to start. It's generally less expensive than permanent (whole) life insurance, and is available in varying time periods with fixed premiums from a one year (annual renewable term) to 20-year (level term) period. Furthermore, term life insurance is sometimes convertible to permanent coverage, providing you with flexibility as your needs change.</p>
    </section>
    <section>
      <h3>Whole Life Insurance</h3>
      <p>Whole life insurance is a form of permanent life insurance that remains in force for your entire lifetime, provided premiums are paid as specified in the policy. Whole life insurance can be an investment opportunity, as many whole life insurance policies also build cash value over time.</p>
    </section>
    <section>
      <h3>Universal Life Insurance</h3>
      <p>Universal life is a form of permanent life insurance characterized by its flexible premiums, face amounts and unbundled pricing structure. Universal life can build cash value, which earns an interest rate that may adjust periodically, but is usually guaranteed not to fall below a certain percentage.</p>
      <p>So what type of life insurance is best for you? Talk with the team at TPVN today at:<br>800-555-0187(TPVN), and we can assist in identifying the best protection for you.</p>
    </section>
    <section>
      <h3>What are the advantages of life insurance?</h3>
      <p>Having the right life insurance is essential to planning for your present, and your future. Not only can life insurance provide assurance for your family after you are gone, many life insurance options offer other benefits and investment opportunities you can take advantage of while you are living.</p>
      <p>Advantages of the life insurance death benefit: When you pass away, your life insurance provides income tax-free money to your named beneficiary or beneficiaries that can be used to pay funeral expenses, debt, tuition, estate taxes or virtually any financial need. Your policy can help provide security for your business security as well, by enabling partners to buy out the interests of a deceased partner and prevent a forced liquidation.</p>
      <p>Advantages of Living Benefits: The cash value growth of a permanent (whole) life insurance policy is tax-deferred, meaning you do not pay taxes on the growth of cash value, unless money is withdrawn. Loans or withdrawals can be taken against the cash value of a permanent life insurance policy to help with expenses, such as college tuition or the down payment on a home.</p>
      <p>The right life insurance coverage for each and every one of our neighbors in California is unique – Call TPVN today to find out how to protect your family and your future with the right life insurance.</p>
    </section>
  </div>

  <aside class="sidebar">
    <div class="quote-box">
      <h4>Get A Free Quote</h4>
      <div class="quote-field"><span>Name:</span><i></i></div>
      <div class="quote-field"><span>Birth Date:</span><i></i></div>
      <div class="quote-field"><span>Policy Type:</span><i></i></div>
      <div class="quote-field"><span>Coverage Amount:</span><i></i></div>
      <div class="quote-btn">Submit</div>
    </div>
    <div class="promo">
      <div class="promo-photo" role="img" aria-label="Photo of a smiling call-center agent wearing a headset"></div>
      <h4>Need A Quote?</h4>
      <p>Our Agents are ready to find out your needs and get you started</p>
      <div class="promo-cta">Get Started Now</div>
    </div>
    <div class="newsletter">
      <h4>Signup For Newsletter</h4>
      <span>Enter email address</span>
      <i></i>
      <div class="news-btn">Submit</div>
    </div>
  </aside>
</section>

<footer class="site-footer">
  TriPoint Valley Insurance Services<br>
  480 W. Orchard Ave. Linden, CA 91850 Phone (555) 014-2250 Fax (555) 014-2251<br>
  License #0473916
</footer>

</body>
</html>
```